Design a LinkedIn Banner for Company & Sales Reps

Task Description:
We are looking for a talented designer to create a modern, eye-catching LinkedIn banner that will be used on our company LinkedIn page, as well as by our sales reps on their individual LinkedIn profiles.
Key Requirements:
Clean, sharp, and professional design
Must include both the QORANE logo (primary) and the SOLWEN NP logo (secondary)
We would like two separate color versions of the same banner:
One that matches QORANE brand colors
One that matches SOLWEN NP brand colors
Layout and design elements can remain the same between both versions — only the color palette should differ
Design Style:
Simple yet sharp and modern
Professional and clean — not overly busy
Visually balanced to highlight both brands appropriately
Target Market(s)
Medical Device Industry & Physicians
Industry/Entity Type
Medical Device / Pain Management
Look and feel

```html
<!DOCTYPE html>
<html lang="en">
<head>
<meta charset="utf-8">
<title>Profile Banner – QORANE &amp; SOLWEN NP</title>
<link href="https://fonts.googleapis.com/css2?family=Poppins:wght@400;500;600;700&display=swap" rel="stylesheet">
<style>
  :root {
    --stage: #3a3a3a;
    --ink: #1a1a1a;
    --qorane-green: #6dbb3c;
    --solwen-purple: #a3238e;
    --solwen-navy: #111a48;
  }
  * { margin: 0; padding: 0; box-sizing: border-box; }
  html, body { width: 1200px; height: 600px; overflow: hidden; background: var(--stage); }
  body { position: relative; font-family: "Poppins", sans-serif; }

  .banner {
    position: absolute;
    left: 125px;
    width: 950px;
    height: 238px;
    overflow: hidden;
    background: var(--bg);
  }
  .banner--green {
    top: 55px;
    --bg: #f1fce9;
    --circle-a: #e2f7d2;
    --circle-b: #c9c9c9;
    --accent: var(--qorane-green);
    --heading: var(--qorane-green);
    --button: var(--qorane-green);
    --dot: #7dc64b;
  }
  .banner--pink {
    top: 308px;
    --bg: #fde5f8;
    --circle-a: #d3e3fd;
    --circle-b: #bdbdbd;
    --accent: var(--qorane-green);
    --heading: var(--solwen-navy);
    --button: var(--solwen-purple);
    --dot: #b03a9b;
  }

  .brand-primary {
    position: absolute;
    left: 9px;
    top: 20px;
    font-weight: 500;
    font-size: 22px;
    line-height: 1;
    color: var(--accent);
  }

  .team-photo {
    position: absolute;
    left: 42px;
    top: 28px;
    width: 294px;
    height: 294px;
    border-radius: 50%;
    background: radial-gradient(circle at 50% 55%, var(--circle-b) 0%, var(--circle-b) 38%, var(--circle-a) 70%);
  }

  .dot-grid { position: absolute; }
  .dot-grid--left { left: 276px; top: -2px; }
  .dot-grid--right { left: 902px; top: 14px; }

  .message {
    position: absolute;
    left: 360px;
    width: 460px;
    top: 64px;
    text-align: center;
  }
  .message__title {
    font-weight: 700;
    font-size: 28.5px;
    line-height: 1.1;
    letter-spacing: -0.4px;
    color: var(--heading);
    white-space: nowrap;
  }
  .message__lead {
    margin-top: 3px;
    font-size: 11.8px;
    color: var(--ink);
  }
  .message__cta {
    display: inline-block;
    margin-top: 9px;
    width: 116px;
    height: 29px;
    line-height: 30px;
    border-radius: 15px;
    background: var(--button);
    color: #fff;
    font-weight: 600;
    font-size: 18px;
  }
  .message__phone {
    margin-top: 5px;
    font-size: 14px;
    color: var(--ink);
  }

  .brand-secondary {
    position: absolute;
    right: 12px;
    top: 196px;
    font-weight: 600;
    font-size: 19px;
    line-height: 1;
    color: var(--solwen-purple);
  }
</style>
</head>
<body>

  <section class="banner banner--green">
    <div class="brand-primary">QORANE</div>
    <div class="team-photo" role="img" aria-label="Black and white photo of three masked medical professionals: a nurse, a doctor with stethoscope and a nurse with clipboard"></div>
    <svg class="dot-grid dot-grid--left" width="62" height="150" aria-hidden="true">
      <defs><pattern id="dots-g1" width="14" height="15" patternUnits="userSpaceOnUse"><circle cx="3" cy="3" r="1.3" fill="var(--dot)"/></pattern></defs>
      <rect width="62" height="150" fill="url(#dots-g1)"/>
    </svg>
    <svg class="dot-grid dot-grid--right" width="48" height="156" aria-hidden="true">
      <defs><pattern id="dots-g2" width="14" height="15" patternUnits="userSpaceOnUse"><circle cx="3" cy="3" r="1.3" fill="var(--dot)"/></pattern></defs>
      <rect width="48" height="156" fill="url(#dots-g2)"/>
    </svg>
    <div class="message">
      <h1 class="message__title">MEDICAL DEVICE &amp; PHYSICIANS</h1>
      <p class="message__lead">Lorem ipsum dolor sit amet adipiscing elit, sed do eiusmod</p>
      <span class="message__cta">CALL US</span>
      <p class="message__phone">+012 3456 7890</p>
    </div>
    <div class="brand-secondary">SOLWEN NP</div>
  </section>

  <section class="banner banner--pink">
    <div class="brand-primary">QORANE</div>
    <div class="team-photo" role="img" aria-label="Black and white photo of three masked medical professionals: a nurse, a doctor with stethoscope and a nurse with clipboard"></div>
    <svg class="dot-grid dot-grid--left" width="62" height="100" aria-hidden="true">
      <defs><pattern id="dots-p1" width="14" height="15" patternUnits="userSpaceOnUse"><circle cx="3" cy="3" r="1.3" fill="var(--dot)"/></pattern></defs>
      <rect width="62" height="100" fill="url(#dots-p1)"/>
    </svg>
    <svg class="dot-grid dot-grid--right" width="48" height="156" aria-hidden="true">
      <defs><pattern id="dots-p2" width="14" height="15" patternUnits="userSpaceOnUse"><circle cx="3" cy="3" r="1.3" fill="var(--dot)"/></pattern></defs>
      <rect width="48" height="156" fill="url(#dots-p2)"/>
    </svg>
    <div class="message">
      <h1 class="message__title">MEDICAL DEVICE &amp; PHYSICIANS</h1>
      <p class="message__lead">Lorem ipsum dolor sit amet adipiscing elit, sed do eiusmod</p>
      <span class="message__cta">CALL US</span>
      <p class="message__phone">+012 3456 7890</p>
    </div>
    <div class="brand-secondary">SOLWEN NP</div>
  </section>

</body>
</html>
```